Lawn Company needs design work on a service call flyer!

We are a lawn care company that fertilizes and sprays lawns. This design is meant to be left behind at the customers house after a lawn application has been done too let them know what we have done.

The finished design will be printed on A6 paper (4.1 x 5.8 inches)

I have attached PDF files of the text that I want on the front of the document and the back of the document. I also included a sample design that I had been working on to give some idea what I would like. I don't want the same design, but you can use it as a building block for something new or come up with something entirely different.

FRONT: The front of the design is most important.

BACK: Other then the text the design should be minimal. If possible I would like an outline of the trees in my logo to be a backdrop. I have attached a PDF of the back of my business card as an example

The winning design will be a professional looking document that flows and reflects a lawn care business. Please contact me if you have any questions. I will only pick a design that is better then my current template.

Thank You

Target Market(s)

Lawn Care Customers

Industry/Entity Type

Lawn Care

Requirements
Must have
• 1. Our Logo
• 2. The attached text for the front & back of document
• 3. Our phone number (604-918-4471)
• 4. Our Email address (fenwickturfcare@mailora.net)
Nice to have
• A green theme with flowing graphics
Should not have
• any pictures of houses, people, or tools
• Don't copy the text or design from my design template. It is outdated, is it meant to be an example only

```html
<!DOCTYPE html>
<html lang="en">
<head>
<meta charset="utf-8">
<title>Fenwick Turf Care – Service Notice</title>
<link rel="stylesheet" href="https://fonts.googleapis.com/css2?family=Arimo:wght@400;700&display=swap">
<style>
  :root {
    --cream-top: #f8f2b8;
    --cream-low: #fffde9;
    --green-dark: #0b5a2e;
    --green-mid: #43a33c;
    --green-light: #8cc84a;
    --green-pale: #c7e29a;
    --text-green: #17693a;
    --contact-green: #2f9a3a;
    --footer-green: #3f9b47;
    --white: #ffffff;
  }
  * { margin: 0; padding: 0; box-sizing: border-box; }
  html, body { width: 1200px; height: 848px; overflow: hidden; background: var(--white); }
  body { font-family: "Arimo", Arial, sans-serif; color: var(--text-green); }
  .notice { position: relative; width: 1200px; height: 848px; overflow: hidden; }
  .header-wave { position: absolute; left: 0; top: 0; width: 1200px; height: 390px; }
  .brand { position: absolute; left: 116px; top: 120px; width: 320px; color: var(--green-dark); font-weight: 700; line-height: 1; }
  .brand-name { display: block; font-size: 46px; letter-spacing: 1px; }
  .brand-sub { display: block; font-size: 46px; letter-spacing: 1px; margin-top: 6px; }
  .contact { position: absolute; color: var(--contact-green); font-weight: 700; display: flex; align-items: center; gap: 14px; }
  .contact-email { left: 684px; top: 44px; font-size: 29px; }
  .contact-phone { left: 802px; top: 92px; font-size: 26px; }
  .contact svg { fill: var(--contact-green); }
  .field { position: absolute; font-size: 22px; display: flex; align-items: flex-end; white-space: nowrap; }
  .blank { display: inline-block; border-bottom: 2px solid var(--text-green); height: 22px; margin-left: 8px; }
  .field-date { left: 710px; top: 330px; }
  .field-date .blank { width: 190px; }
  .field-tech { left: 88px; top: 413px; }
  .field-tech .blank { width: 562px; margin-left: 8px; }
  .intro { position: absolute; left: 253px; top: 482px; font-size: 21px; }
  .options { position: absolute; left: 267px; top: 534px; list-style: none; }
  .option { display: flex; align-items: center; height: 22px; margin-bottom: 30px; font-size: 21px; }
  .checkbox { width: 23px; height: 23px; border: 1.5px solid var(--green-light); margin-right: 13px; flex: none; }
  .option .note { margin-left: 12px; }
  .option .blank { width: 168px; }
  .field-water { left: 253px; top: 714px; font-size: 21px; }
  .field-water .blank { width: 168px; margin: 0 6px 0 12px; }
  .footer { position: absolute; left: 0; top: 797px; width: 1200px; height: 51px; background: var(--footer-green); color: var(--white); font-size: 13.4px; line-height: 17px; text-align: center; padding: 7px 14px 0; }
</style>
</head>
<body>
<main class="notice">
  <svg class="header-wave" viewBox="0 0 1200 390" aria-hidden="true">
    <defs>
      <linearGradient id="cream" x1="0" y1="0" x2="0" y2="1">
        <stop offset="0" stop-color="#f8f2b8"/>
        <stop offset="1" stop-color="#fffde9"/>
      </linearGradient>
      <linearGradient id="paleFade" x1="0" y1="0" x2="0" y2="1">
        <stop offset="0" stop-color="#a9d56c"/>
        <stop offset="1" stop-color="#eef6e0"/>
      </linearGradient>
    </defs>
    <rect width="1200" height="390" fill="url(#cream)"/>
    <path d="M0,214 C260,262 600,250 880,190 C1030,158 1130,152 1200,190 L1200,390 L0,390 Z" fill="url(#paleFade)"/>
    <path d="M0,214 C260,262 600,250 880,190 C1030,158 1130,152 1200,190 L1200,196 C1120,172 1020,178 880,226 C620,312 300,346 0,330 Z" fill="#7dbf3f"/>
    <path d="M0,262 C300,302 600,276 880,200 C1000,168 1090,162 1180,176 C1080,172 990,190 880,226 C640,306 320,330 0,306 Z" fill="#0b5a2e"/>
    <path d="M0,306 C320,330 640,306 880,226 C990,190 1080,172 1180,176 C1100,186 1010,210 900,252 C660,344 330,370 0,352 Z" fill="#8cc84a"/>
    <path d="M0,364 C340,388 700,340 960,250 C1070,212 1150,198 1200,200 L1200,390 L0,390 Z" fill="#ffffff"/>
  </svg>

  <div class="brand">
    <span class="brand-name">FENWICK</span>
    <span class="brand-sub">TURF CARE</span>
  </div>

  <div class="contact contact-email">
    <svg width="24" height="16" viewBox="0 0 24 16" aria-hidden="true"><path d="M0,0 H24 V16 H0 Z M2,2 L12,9 L22,2 Z" fill-rule="evenodd"/></svg>
    fenwickturfcare@mailora.net
  </div>
  <div class="contact contact-phone">
    <svg width="24" height="20" viewBox="0 0 24 20" aria-hidden="true"><path d="M1,5 C6,0 18,0 23,5 L21,8 L17,6 L17,4 C14,3 10,3 7,4 L7,6 L3,8 Z M6,9 H18 L21,19 H3 Z"/></svg>
    604-918-4471
  </div>

  <div class="field field-date">Application Time/Date:<span class="blank"></span></div>
  <div class="field field-tech">Your lawn has been proffessionally serviced by:<span class="blank"></span></div>

  <p class="intro">Today's application consists of</p>
  <ul class="options">
    <li class="option"><span class="checkbox"></span>Seasonally Balanced Slow Release Fertilizer</li>
    <li class="option"><span class="checkbox"></span>Broadleaf Weed Control<span class="note">(Please keep off the lawn until it is thoroughly dry)</span></li>
    <li class="option"><span class="checkbox"></span>Other<span class="blank"></span></li>
  </ul>

  <div class="field field-water">Please begin watering the lawn<span class="blank"></span>after application</div>

  <footer class="footer">* We strive to complete work in a professional manner each and every visit. If you are not satisfied with the level of service you are receiving please contact us. We value your business and wish to maintain long-term relationships with our customers.</footer>
</main>
</body>
</html>
```